Tau Omicron civil engineering orgnization activities flyer

we need flyer design for Tau Omicron civil engineering honor society in Halverton College for mining and industry. the flyer contain the schedule of the expected activity. the design should have a purple color and Tau Omicron Key and logo (you will find them in the attached file) and the design should have something referring to civil engineering

Industry/Entity Type

Education

Colors
6b449b

Requirements
Must have
• Tau Omicron logo, key, motto
Nice to have
• civil engineering samples, purple color

```html
<!DOCTYPE html>
<html lang="en">
<head>
<meta charset="utf-8">
<title>Tau Omicron – Activities Flyer</title>
<link rel="stylesheet" href="https://fonts.googleapis.com/css2?family=PT+Sans:wght@400;700&display=swap">
<style>
:root{
  --page:#2e2e2e;
  --ink-dark:#241640;
  --purple-deep:#2f1f57;
  --purple-table:#3b2a6a;
  --purple-mid:#6b449b;
  --purple-soft:#7a55aa;
  --gold:#e0a92a;
  --white:#ffffff;
  --text:#333333;
  --grid:rgba(255,255,255,.75);
}
*{box-sizing:border-box;margin:0;padding:0}
html,body{width:1200px;height:1200px;overflow:hidden;background:var(--page);font-family:"PT Sans",Arial,sans-serif}
.flyer{position:absolute;left:174px;top:50px;width:852px;height:1100px;background:var(--purple-deep);overflow:hidden}
.block{position:absolute}
.hero-photo{left:0;top:0;width:852px;height:382px;background:linear-gradient(160deg,#8c7d8e 0%,#5c4f6e 40%,#3a2d5a 75%,#2f1f57 100%)}
.skyline-photo{left:278px;top:180px;width:152px;height:202px;background:linear-gradient(180deg,#2b3a6e 0%,#6a5a7a 45%,#d07a3a 55%,#1a1628 62%,#0d0c14 100%)}
.title-box{left:430px;top:180px;width:422px;height:202px;background:var(--ink-dark);color:var(--white);text-align:center;font-weight:700;line-height:.9;padding-top:16px}
.title-box .t1{font-size:54px;display:block;letter-spacing:.5px}
.title-box .t2{font-size:90px;display:block;letter-spacing:1px}
.title-box .t3{font-size:50px;display:block}
.gridlines{left:0;top:0;width:852px;height:1100px;pointer-events:none}
.meeting{left:0;top:382px;width:852px;height:216px;background:linear-gradient(90deg,var(--purple-deep),var(--purple-table))}
.meeting-label{position:absolute;left:10px;top:200px;transform:rotate(-90deg);transform-origin:left top;color:var(--white);font-weight:700;font-size:44px;letter-spacing:1px}
.schedule{position:absolute;left:72px;top:13px;width:744px;border-collapse:collapse;font-size:15.5px;color:var(--white)}
.schedule th,.schedule td{border:1px solid rgba(255,255,255,.35);height:24px;padding:0 12px;text-align:left;font-weight:400}
.schedule th{color:var(--gold);font-weight:700}
.events{left:0;top:598px;width:430px;height:297px;background:linear-gradient(180deg,var(--purple-mid),var(--purple-soft));color:var(--white);padding:8px 12px 0 26px;font-size:13.3px;line-height:16px}
.events h2{color:var(--gold);font-size:19px;line-height:20px;font-weight:700}
.events p{margin-bottom:9px}
.events .hl{color:var(--gold);font-weight:700}
.events b{font-weight:700}
.initiation{left:0;top:895px;width:430px;height:70px;background:var(--purple-deep);color:var(--white);font-weight:700;font-size:16px;line-height:20px;padding:6px 10px 0 26px;display:flex;gap:26px}
.initiation .lbl{color:var(--gold);font-size:19px}
.about{left:430px;top:598px;width:422px;height:366px;background:var(--white);color:var(--text);font-size:12.9px;line-height:16px;padding:10px 22px 0 14px}
.about p{margin-bottom:10px}
.footer-name{left:18px;top:968px;width:412px;height:110px;background:var(--white);display:flex;align-items:center;justify-content:center;gap:12px}
.footer-name .mark{width:22px;height:22px;border-radius:50%;background:var(--purple-mid)}
.footer-name .name{color:var(--purple-mid);font-weight:700;font-size:46px}
.contact{left:432px;top:968px;width:300px;height:110px;background:linear-gradient(90deg,#2a1c48,#4a3670);color:var(--white);font-size:14.5px;line-height:20px;padding:28px 8px 0 0;text-align:right}
.contact .gold{color:var(--gold)}
.contact .sq{display:inline-block;width:11px;height:11px;background:var(--gold);margin-right:5px;vertical-align:-1px}
.contact svg{vertical-align:-2px;margin-right:4px}
.chapter-mark{left:732px;top:968px;width:96px;height:110px;background:var(--white);color:var(--purple-deep);font-weight:700;text-align:center;display:flex;flex-direction:column;justify-content:center;font-size:12px;line-height:15px;white-space:nowrap}
.chapter-mark .square{width:40px;height:40px;border:3px solid var(--purple-deep);margin:6px auto}
</style>
</head>
<body>
<div class="flyer">
  <div class="block hero-photo" role="img" aria-label="Photo of two engineers in hard hats on a construction site, one pointing ahead"></div>
  <div class="block skyline-photo" role="img" aria-label="Photo of a city skyline lit at dusk below mountains"></div>
  <div class="block title-box">
    <span class="t1">CONCEPTION</span>
    <span class="t2">DESIGN</span>
    <span class="t3">CONSTRUCTION</span>
  </div>

  <section class="block meeting">
    <div class="meeting-label">MEETING</div>
    <table class="schedule">
      <colgroup><col style="width:48px"><col style="width:110px"><col style="width:72px"><col style="width:142px"><col style="width:210px"><col></colgroup>
      <tr><th>No.</th><th>Date</th><th>Time</th><th>Location</th><th>Name</th><th>Company</th></tr>
      <tr><td>1</td><td>9/8/2015</td><td>7 PM</td><td>BCH 124</td><td>Dr. Hartwell</td><td></td></tr>
      <tr><td>2</td><td>9/22/2015</td><td>7 PM</td><td>BCH 124</td><td>Neil Carrow</td><td>Metro Waterworks</td></tr>
      <tr><td>3</td><td>10/6/2015</td><td>7 PM</td><td>BCH 124</td><td>Owen Patridge</td><td>Camp Ridgeford</td></tr>
      <tr><td>4</td><td>10/20/2015</td><td>7 PM</td><td>BCH 124</td><td>Jamie Colfax</td><td>Norvel Inc.</td></tr>
      <tr><td>5</td><td>11/3/2015</td><td>7 PM</td><td>BCH 124</td><td>Scavenger Hunt</td><td>Social</td></tr>
      <tr><td>6</td><td>11/17/2015</td><td>7 PM</td><td>BCH124</td><td>Nomination/Ray Tolliver</td><td>Brightline Advisors</td></tr>
      <tr><td>7</td><td>12/1/2015</td><td>7 PM</td><td>BCH 124</td><td>Elections</td><td>-</td></tr>
    </table>
  </section>

  <section class="block events">
    <h2>SERVICE</h2>
    <p><span class="hl">Linden Creek Preserve Service Day</span> / Saturday, Oct 24, 11 am / Linden Creek Preserve, Halverton, MO 65490, United States</p>
    <p><span class="hl">Community Alliance Service Day</span> / Saturday, Nov 7, 11 am / The Community Alliance Resale Shop, 2140 N Cedar Ave, Halverton, MO 65490, United States</p>
    <p><span class="hl">Tri-Valley Animal Shelter Volunteer Day</span> / Thursday, Nov 12, 12 pm / Tri-Valley Animal Shelter, 812 E Maple St, Westbury, MO 65572, United States</p>
    <h2>SOCIAL</h2>
    <p><b>Tau Omicron Smoker</b> (Tuesday, September 29th at Noon in BCH 120)</p>
    <p><b>Bowling / Starlite Lanes</b> (1420 Ridge Road)/ Wednesday, October 28th /9:00 PM</p>
    <p><b>Plaque Signing/ When:</b> December 8th / the Zone</p>
  </section>

  <section class="block initiation">
    <span class="lbl">Initiation</span>
    <span>12/12/2015 &nbsp;&nbsp; 5 PM-6PM &nbsp;&nbsp;BCH 314<br>6:30PM initiation diner / Marlowe's- 1250<br>North Fulton Street, Westbury,</span>
  </section>

  <section class="block about">
    <p>We are dedicated to the purpose of maintaining and promoting the status of civil engineering as an ideal profession. Tau Omicron was organized to recognize the characteristics of the individual civil engineer deemed to be fundamental to the successful pursuit of an engineering career, and to aid in the development of those characteristics in civil engineering students.</p>
    <p>Engineering, the application of scientific principles to the practical needs of society, is assuming a constantly increasing responsibility for the well-being of all people, and thus calling for competence of the highest order. This responsibility can be discharged only by a professional group whose members who possess a good basic technical ability, intelligence, moral integrity, and effective social poise in their relationship with the larger community of which they are part.</p>
    <p>To contribute to the improvement of the profession, Tau Omicron fosters the development and exercise of sound traits of character and technical ability among civil engineers, and its members, by precept and example, toward an ever higher standard of professional service.</p>
  </section>

  <div class="block footer-name">
    <span class="mark"></span>
    <span class="name">Tau Omicron</span>
  </div>

  <div class="block contact">
    <span class="gold">Orgsite:</span> https://orgsite.net/40217/chapter<br>
    <span class="sq"></span>https://www.friendspace.net/to.hcmi<br>
    <svg width="13" height="13" viewBox="0 0 14 14" fill="none" stroke="#e0a92a" stroke-width="1.3"><circle cx="7" cy="7" r="6"/><ellipse cx="7" cy="7" rx="2.6" ry="6"/><path d="M1 7h12"/></svg>www.tau-omicron.org
  </div>

  <div class="block chapter-mark">
    <span>TAU OMICRON</span>
    <span class="square"></span>
    <span>TAU GAMMA TAU</span>
  </div>

  <svg class="block gridlines" width="852" height="1100" viewBox="0 0 852 1100">
    <g stroke="var(--grid)" stroke-width="1" fill="none">
      <line x1="54" y1="0" x2="54" y2="382"/>
      <line x1="278" y1="0" x2="278" y2="382"/>
      <line x1="430" y1="0" x2="430" y2="382"/>
      <line x1="816" y1="0" x2="816" y2="180"/>
      <line x1="0" y1="180" x2="852" y2="180"/>
      <line x1="0" y1="382" x2="852" y2="382"/>
      <line x1="18" y1="382" x2="18" y2="1100"/>
      <line x1="0" y1="598" x2="852" y2="598"/>
      <line x1="0" y1="966" x2="852" y2="966"/>
      <line x1="0" y1="1080" x2="852" y2="1080"/>
      <line x1="430" y1="966" x2="430" y2="1100"/>
      <line x1="828" y1="966" x2="828" y2="1100"/>
    </g>
  </svg>
</div>
</body>
</html>
```